Bramwell's Mobile Transport

we would like a new logo for our mobile home transport company we are based in Colorado . what we would like is a mobile home toter ( truck) in a stylish piece of art work Haling a mobile home behind it from a left to right 3-d view, so that you can see the front of the truck and the whole left side of the truck and mobile home, the truck colors are an emerald green and white two-tone the top half the emerald green and the bottom half is to be white, and would like to see something creative with the name of the company as in style please nothing clesha as in with the Irish culture. please see attached examples of truck and truck artwork style.

It Company

00a990

```html
<!DOCTYPE html>
<html lang="en">
<head>
<meta charset="utf-8">
<title>Bramwell's Mobile Transport – Business Card</title>
<link rel="stylesheet" href="https://fonts.googleapis.com/css2?family=Nunito:wght@400;700&display=swap">
<style>
  :root {
    --bg: #000000;
    --green-light: #12a64e;
    --green: #0f9a47;
    --green-dark: #0b6b36;
    --green-text: #0e8f43;
    --white: #ffffff;
    --gold-line: #c9bf9c;
    --truck-green: #1a9a4a;
    --truck-white: #e9ecef;
    --roof-red: #b3261e;
  }
  * { margin: 0; padding: 0; box-sizing: border-box; }
  html, body { width: 1200px; height: 1000px; overflow: hidden; background: var(--bg); }
  .canvas { position: relative; width: 1200px; height: 1000px; }

  .card { position: absolute; overflow: hidden; }
  .card--front {
    left: 240px; top: 73px; width: 706px; height: 413px;
    background: linear-gradient(90deg, var(--green-light) 0%, var(--green) 55%, var(--green-dark) 100%);
  }
  .card--back { left: 244px; top: 512px; width: 702px; height: 410px; background: var(--white); }

  .truck-art {
    position: absolute; border-radius: 18px 40px 28px 30px;
    background: linear-gradient(180deg, var(--roof-red) 0%, var(--roof-red) 14%, var(--truck-green) 14%, var(--truck-green) 45%, var(--truck-white) 45%, #b9c0c6 100%);
  }
  .card--front .truck-art { left: 58px; top: 103px; width: 255px; height: 175px; }
  .card--back .truck-art { left: 440px; top: 50px; width: 203px; height: 138px; }

  .company-name {
    position: absolute; font-family: "Nunito", sans-serif; font-weight: 700;
    font-size: 24px; line-height: 1; white-space: nowrap;
  }
  .card--front .company-name { left: 330px; top: 178px; color: var(--white); }
  .card--back .company-name { left: 40px; top: 107px; color: var(--green-text); }

  .web-band {
    position: absolute; left: 0; top: 357px; width: 100%; height: 31px;
    background: var(--white); display: flex; align-items: center; justify-content: center; gap: 6px;
    font-family: "Nunito", sans-serif; font-weight: 700; font-size: 18px; color: var(--green-text);
  }

  .contact-panel {
    position: absolute; left: 0; top: 220px; width: 100%; height: 190px;
    background: linear-gradient(90deg, var(--green-light) 0%, var(--green) 50%, var(--green-dark) 100%);
    color: var(--white); font-family: "Nunito", sans-serif;
  }
  .contact-panel::before {
    content: ""; position: absolute; left: 0; top: -6px; width: 100%; height: 4px;
    background: linear-gradient(90deg, rgba(201,191,156,0) 0%, var(--gold-line) 40%, var(--gold-line) 100%);
  }
  .owner-name { position: absolute; left: 26px; top: 8px; font-weight: 700; font-size: 23px; }
  .owner-role { position: absolute; left: 26px; top: 42px; font-size: 21px; }
  .contact-list { position: absolute; left: 26px; top: 87px; list-style: none; font-size: 19px; line-height: 26px; }
  .contact-list li { display: flex; align-items: center; gap: 6px; }
  .contact-list svg { flex: none; }
  .address {
    position: absolute; right: 26px; top: 87px; text-align: right;
    font-style: normal; font-size: 19px; line-height: 26px;
  }
</style>
</head>
<body>
<div class="canvas">

  <section class="card card--front">
    <div class="truck-art" role="img" aria-label="Illustration of a green and white truck hauling a mobile home with a red roof"></div>
    <h1 class="company-name">Bramwell's Mobile Transport</h1>
    <div class="web-band">
      <svg width="16" height="16" viewBox="0 0 16 16" fill="none" stroke="currentColor" stroke-width="1.3">
        <circle cx="8" cy="8" r="6.5"/><ellipse cx="8" cy="8" rx="3" ry="6.5"/><line x1="1.5" y1="8" x2="14.5" y2="8"/>
      </svg>
      <span>www.bramwelltowingandrecovery.com</span>
    </div>
  </section>

  <section class="card card--back">
    <h2 class="company-name">Bramwell's Mobile Transport</h2>
    <div class="truck-art" role="img" aria-label="Illustration of a green and white truck hauling a mobile home with a red roof"></div>

    <div class="contact-panel">
      <p class="owner-name">Dale and Rena Bramwell</p>
      <p class="owner-role">Owners</p>
      <ul class="contact-list">
        <li>
          <svg width="14" height="16" viewBox="0 0 14 16" fill="none" stroke="currentColor" stroke-width="1.4">
            <rect x="3" y="1" width="8" height="14" rx="1.5"/><line x1="6" y1="12.5" x2="8" y2="12.5"/>
          </svg>
          <span>555 210 4476</span>
        </li>
        <li>
          <svg width="16" height="16" viewBox="0 0 16 16" fill="none" stroke="currentColor" stroke-width="1.4">
            <rect x="4" y="1.5" width="8" height="4"/><rect x="1.5" y="5.5" width="13" height="6"/><rect x="4" y="9.5" width="8" height="5" fill="currentColor"/>
          </svg>
          <span>555 210 4490</span>
        </li>
        <li>
          <svg width="18" height="14" viewBox="0 0 18 14" fill="none" stroke="currentColor" stroke-width="1.4">
            <rect x="1" y="1.5" width="16" height="11"/><polyline points="1,1.5 9,8 17,1.5"/>
          </svg>
          <span>bramwellsmobiletransport@mailbox.com</span>
        </li>
      </ul>
      <address class="address">
        4820 N<br>
        Ridgeline Road<br>
        Elbert Valley, CO 80099
      </address>
    </div>
  </section>

</div>
</body>
</html>
```